Non-profit organisation for street children in Indonesia

Lentera Bocah provides home, education, family and health care for street children and other underprivileged children in Indonesia.

We need an emotional catchy advertisement that will make people aware of the terrible living conditions of street children in Indonesia and the great work the Lentera Bocah Foundation is doing to help these children.

We have 1 photo available for this advertisement. A little girl laying in the streets. This photo can be used with a strong quote such as "Street children whose responsibility?" or "Safer out on streets than at home" or "This child doesn't have the right to have a childhood worth remembering?" or another strong quote. Be creative! It need to touch people!

See some similar advertisements of other non-profit organizations what we very much like:

http://7brightpix.example/wp-content/uploads/2011/07/boldposters41.jpg
http://7brightpix.example/wp-content/uploads/2011/07/affiches-nobles-motifs-058.jpg

Mission
To give every child in the world the opportunity to live a happy and healthy life free of poverty, exploitation, and violence.

Overview
Lentera Bocah Foundation is an independent non-governmental organisation founded in 2005 in the Netherlands and expanded to Indonesia in 2006. Our aim is to improve the lives of children and to protect their rights by providing education, accommodation, family care and medical and legal aid.

Description
Lentera Bocah (Light for Youngsters) Foundation serves homeless and impoverished children by offering them a new path in life. By providing them with the necessary shelter, education, and psychological support directed towards vocational training, mentorship, and micro-credit opportunities, it strives to enable their re-entery into the community as happy and self-sufficient adults.

Facts:
There are 70 million children in Indonesia, nearly 18 million are very poor and estimated 170,000 children live on the streets.

Pitch submissions need to be 960x696 pixels.

Files available 1 photo and logo
Updates

Reason: Dear Designers, We have decided to extend the deadline because we haven't received what we are after. Please make a design in the trend as the following two examples: http://7brightpix.example/wp-content/uploads/2011/07/boldposters41.jpg http://7brightpix.example/wp-content/uploads/2011/07/affiches-nobles-motifs-058.jpg We hope to receive a good design shortly! Thank you Kind regards Lentera Bocah

Target Market(s)

Everybody

Industry/Entity Type

Non-Profit

Requirements
Must have
• 1. A strong quote.
2. Website url: www.lenterabocah.org
3. Mission quote from Lentera Bocah:
Should not have
• To much text.

```html
<!DOCTYPE html>
<html lang="en">
<head>
<meta charset="utf-8">
<title>Lentera Bocah Foundation – Street Children Whose Responsibility?</title>
<link href="https://fonts.googleapis.com/css2?family=Righteous&family=Jost:wght@400&family=Arimo:wght@400&display=swap" rel="stylesheet">
<style>
  :root {
    --green-glow: #08a04e;
    --green-mid: #0b7a48;
    --green-deep: #0c4a3d;
    --yellow: #f3d21a;
    --white: #ffffff;
    --photo-light: #dfe4e2;
    --photo-warm: #9a7256;
  }
  * { margin: 0; padding: 0; box-sizing: border-box; }
  html, body { width: 870px; height: 1200px; overflow: hidden; }
  body { background: var(--green-deep); }
  .poster {
    position: relative;
    width: 870px;
    height: 1200px;
    overflow: hidden;
    background: radial-gradient(ellipse 620px 700px at 400px 470px, var(--green-glow) 0%, var(--green-mid) 40%, var(--green-deep) 85%);
  }
  .brand {
    position: absolute;
    top: 48px;
    right: 58px;
    display: flex;
    align-items: center;
    gap: 10px;
    color: var(--yellow);
    font-family: "Righteous", sans-serif;
  }
  .brand-name { font-size: 24px; line-height: 1; text-align: right; }
  .brand-name small { display: block; font-size: 15px; }
  .brand-dot { width: 34px; height: 34px; border-radius: 50%; background: var(--yellow); }
  .intro {
    position: absolute;
    top: 136px;
    right: 58px;
    text-align: right;
    color: var(--yellow);
  }
  .question {
    font-family: "Righteous", sans-serif;
    font-weight: 400;
    text-transform: uppercase;
    line-height: 1.02;
    letter-spacing: 0.5px;
  }
  .question .line-1 { display: block; font-size: 28px; }
  .question .line-2 { display: block; font-size: 32px; }
  .mission {
    margin-top: 14px;
    font-family: "Arimo", sans-serif;
    font-size: 15.2px;
    line-height: 1.2;
  }
  .donate {
    margin-top: 12px;
    font-family: "Arimo", sans-serif;
    font-size: 10px;
    line-height: 1.25;
  }
  .dream {
    position: absolute;
    top: 602px;
    right: 56px;
    text-align: right;
    color: var(--white);
    font-family: "Jost", sans-serif;
    font-weight: 400;
    font-size: 63px;
    line-height: 50px;
    text-transform: uppercase;
    letter-spacing: -0.5px;
  }
  .dream span { display: block; }
  .child-photo {
    position: absolute;
    left: 24px;
    top: 494px;
    width: 514px;
    height: 706px;
    background:
      radial-gradient(ellipse 60% 45% at 42% 22%, rgba(154,114,86,0.55) 0%, rgba(154,114,86,0) 100%),
      radial-gradient(ellipse 75% 65% at 45% 75%, rgba(223,228,226,0.85) 0%, rgba(223,228,226,0) 100%);
  }
</style>
</head>
<body>
  <main class="poster">
    <div class="brand">
      <div class="brand-name"><small>Foundation</small>LENTERA BOCAH</div>
      <div class="brand-dot"></div>
    </div>

    <section class="intro">
      <h1 class="question">
        <span class="line-1">Street children whose</span>
        <span class="line-2">responsibility?</span>
      </h1>
      <p class="mission">To give every child in the world the opportunity to live<br>a happy and healthy life free of poverty, exploitation,<br>and violence.</p>
      <p class="donate">Donate to GIRO 4720 t.a.v. Stichting Lentera Bocah<br>or financial adopt a child on www.lenterabocah.org</p>
    </section>

    <div class="child-photo" role="img" aria-label="Photo of a young boy in an oversized white doctor's coat holding a stethoscope"></div>

    <h2 class="dream">
      <span>He want</span>
      <span>to become</span>
      <span>a doctor</span>
    </h2>
  </main>
</body>
</html>
```